QuillHarbor New Website

QuillHarbor is a digital marketing agency. Our clients are all limousine companies. We need a responsive website designed to highlight our services and products. Our competition is http://www.velmorastudiohub.com/ and we need a site of similar design and layout without being too similar. Our old website www.quillharbor.com, is very outdated and the logo and graphics have changed. We will adjust the content to work with the new design. The new logo is attached.

Industry/Entity Type

Digital

Coding

Coded - Design and coding required

```html
<!DOCTYPE html>
<html lang="en">
<head>
<meta charset="utf-8">
<title>QuillHarbor — Digital Marketing</title>
<link href="https://fonts.googleapis.com/css2?family=Lato:ital,wght@0,300;0,400;0,700;1,400;1,700&family=Roboto:ital,wght@1,700&display=swap" rel="stylesheet">
<style>
:root{
  --navy:#0b4562;
  --navy-deep:#083a53;
  --blue:#13608a;
  --gold:#b09a32;
  --gold-field:#a89632;
  --ink:#2b2b2b;
  --muted:#6a7580;
  --paper:#ffffff;
  --face-l:#f1f1f1;
  --face-r:#e2e2e2;
  --footer-text:#dfe7ec;
}
*{margin:0;padding:0;box-sizing:border-box}
html,body{width:701px;height:1200px;overflow:hidden;background:var(--paper)}
body{font-family:"Lato",Arial,sans-serif;color:var(--ink);position:relative}
.canvas-art{position:absolute;left:0;top:0}
.abs{position:absolute}

/* header */
.top-rule{left:0;top:0;width:701px;height:3px;background:var(--navy)}
.brand{left:20px;top:14px;display:flex;align-items:center;gap:8px}
.brand-square{width:14px;height:14px;background:var(--navy)}
.brand-name{font-weight:400;font-size:28px;color:var(--navy);line-height:34px}
.phone{left:575px;top:14px;display:flex;align-items:center;gap:5px;font-size:13px;color:var(--ink)}
.nav{right:20px;top:52px;display:flex;gap:12px;font-size:9.5px;font-weight:700;color:var(--ink);letter-spacing:.2px}

/* hero */
.hero-line{left:178px;top:144px;font-size:15.5px;font-weight:700;font-style:italic;color:#1e2c38;line-height:23px}
.hero-line .accent{font-weight:400;color:var(--navy)}
.hero-line .accent b{color:var(--gold);font-weight:400}
.btn{display:flex;align-items:center;height:14px;font-size:9px;color:#fff}
.btn .tip{width:14px;height:14px;background:var(--gold);display:flex;align-items:center;justify-content:center}
.btn .label{background:var(--navy);height:14px;padding:0 6px;line-height:14px}

/* services */
.svc-label{font-family:"Roboto",Arial,sans-serif;font-style:italic;font-weight:700;font-size:11.5px;color:#fff;width:160px;text-align:center}
.section-title{font-style:italic;font-size:19px;color:#222;width:200px;text-align:center}

/* welcome */
.welcome{left:20px;top:603px;width:320px}
.welcome h2{font-weight:400;font-size:20px;color:#222;padding-bottom:4px;border-bottom:2px solid #999}
.welcome p{font-size:9.6px;line-height:14px;margin-top:7px;text-align:justify;color:#333}

/* quick contact */
.contact{left:368px;top:608px;width:311px;height:171px;background:var(--navy)}
.contact h3{font-weight:400;font-style:italic;font-size:18px;color:#fff;position:absolute;left:13px;top:8px}
.contact .rule{position:absolute;left:13px;top:34px;width:285px;height:1px;background:#6c8ea0}
.field{position:absolute;left:13px;width:210px;background:#fff;font-size:8px;font-style:italic;color:#333;padding:4px 7px}
.send{position:absolute;left:235px;top:131px;width:62px;height:29px;background:var(--gold);color:var(--navy);font-weight:700;font-size:14px;display:flex;align-items:center;justify-content:center;border-radius:2px}

/* gold section */
.col-title{font-style:italic;font-size:18px;color:#fff}
.post-date{font-size:9.5px;color:#222}
.post-text{font-size:9px;font-style:italic;color:#fff;line-height:13px;width:250px}
.event-title{font-size:10.5px;font-weight:700;color:#1f2a30}
.divider{height:1px;border-top:1px dotted rgba(255,255,255,.55)}

/* footer */
.foot-nav{left:20px;top:1106px;display:flex;gap:5px;font-size:9.5px;color:#fff;text-transform:uppercase}
.foot-social{left:20px;top:1134px;display:flex;align-items:center;gap:10px;font-size:10.5px;font-style:italic;color:#fff}
.foot-brand{left:545px;top:1108px;display:flex;align-items:center;gap:7px}
.foot-brand .brand-square{width:11px;height:11px;background:var(--footer-text)}
.foot-brand .brand-name{font-size:22px;color:var(--footer-text);line-height:28px}
.foot-rule{left:20px;top:1166px;width:661px;height:1px;background:#2f6280}
.copyright{left:0;top:1174px;width:701px;text-align:center;font-size:9.5px;color:#fff}
</style>
</head>
<body>

<svg class="canvas-art" width="701" height="1200" viewBox="0 0 701 1200">
  <defs>
    <linearGradient id="hero-tone" x1="0" y1="0" x2="1" y2="0">
      <stop offset="0" stop-color="#7d95ab"/>
      <stop offset=".45" stop-color="#b9c9d6"/>
      <stop offset=".8" stop-color="#8fb1cf"/>
      <stop offset="1" stop-color="#4a6c8c"/>
    </linearGradient>
    <linearGradient id="header-tone" x1="0" y1="0" x2="0" y2="1">
      <stop offset="0" stop-color="#fbfbfb"/>
      <stop offset="1" stop-color="#eceef0"/>
    </linearGradient>
  </defs>

  <rect x="0" y="3" width="701" height="71" fill="url(#header-tone)"/>
  <rect x="0" y="74" width="701" height="220" fill="url(#hero-tone)" role="img" aria-label="Hero photo: a hand touching a glowing digital interface"/>
  <polygon points="0,215 701,215 701,290 350,368 0,290" fill="var(--navy)" opacity=".96"/>

  <circle cx="40" cy="228" r="22" fill="var(--navy-deep)"/>
  <path d="M43 222 L37 228 L43 234" stroke="#fff" stroke-width="2.5" fill="none"/>
  <circle cx="661" cy="228" r="22" fill="var(--navy-deep)"/>
  <path d="M658 222 L664 228 L658 234" stroke="#fff" stroke-width="2.5" fill="none"/>

  <g class="service-block">
    <polygon points="18,378 129,413 129,503 18,468" fill="var(--face-l)"/>
    <polygon points="129,413 240,378 240,468 129,503" fill="var(--face-r)"/>
    <polygon points="18,378 129,343 240,378 129,413" fill="var(--blue)" stroke="var(--navy)" stroke-width="3"/>
  </g>
  <g class="service-block">
    <polygon points="461,378 572,413 572,503 461,468" fill="var(--face-l)"/>
    <polygon points="572,413 683,378 683,468 572,503" fill="var(--face-r)"/>
    <polygon points="461,378 572,343 683,378 572,413" fill="var(--blue)" stroke="var(--navy)" stroke-width="3"/>
  </g>
  <g class="service-block">
    <polygon points="240,290 350,325 350,415 240,380" fill="var(--face-l)"/>
    <polygon points="350,325 461,290 461,380 350,415" fill="var(--face-r)"/>
    <polygon points="240,290 350,255 461,290 350,325" fill="var(--blue)" stroke="var(--navy)" stroke-width="3"/>
  </g>
  <g class="service-block">
    <polygon points="240,465 350,500 350,590 240,555" fill="var(--face-l)"/>
    <polygon points="350,500 461,465 461,555 350,590" fill="var(--face-r)"/>
    <polygon points="240,465 350,430 461,465 350,500" fill="var(--gold)" stroke="#9a8525" stroke-width="3"/>
  </g>

  <g fill="var(--navy)">
    <circle cx="395" cy="342" r="5"/><circle cx="406" cy="339" r="5.5"/><circle cx="418" cy="342" r="5"/>
    <path d="M386 365 q0-14 9-14 q9 0 9 14z"/><path d="M396 365 q0-17 10-17 q10 0 10 17z"/><path d="M409 365 q0-14 9-14 q9 0 9 14z"/>
  </g>
  <g fill="none" stroke="var(--navy)" stroke-width="3">
    <path d="M166 440 a15 15 0 1 1 20 16"/>
    <path d="M168 446 l9 -9 l6 6 l12 -13"/>
  </g>
  <g fill="none" stroke="var(--navy)" stroke-width="2.2">
    <path d="M612 430 h16 a6 6 0 0 1 6 6 v8 a6 6 0 0 1-6 6 h-8 l-7 6 v-6 a6 6 0 0 1-6-6 v-8 a6 6 0 0 1 5-6z"/>
    <path d="M632 425 h10 a4 4 0 0 1 4 4 v6 a4 4 0 0 1-4 4 v4 l-5-4"/>
  </g>
  <g fill="var(--navy)"><circle cx="618" cy="440" r="1.5"/><circle cx="623" cy="440" r="1.5"/><circle cx="628" cy="440" r="1.5"/></g>
  <g fill="none" stroke="var(--gold)" stroke-width="2">
    <rect x="400" y="511" width="13" height="22" rx="2"/>
    <line x1="404" y1="529" x2="409" y2="529"/>
    <circle cx="416" cy="517" r="2.5"/>
    <line x1="391" y1="519" x2="397" y2="519"/><line x1="393" y1="523" x2="397" y2="523"/>
  </g>

  <polygon points="0,893 350,790 701,893 701,1090 0,1090" fill="var(--gold-field)"/>
  <polygon points="242,858 350,824 460,858 350,844" fill="#c4b469" opacity=".7"/>
  <line x1="350" y1="905" x2="350" y2="1060" stroke="#978626" stroke-width="1"/>

  <polygon points="0,1090 244,1090 350,1058 458,1090 701,1090 701,1200 0,1200" fill="var(--navy)"/>

  <g fill="none" stroke="#fff" stroke-width="1.5">
    <circle cx="305" cy="913" r="6"/><circle cx="322" cy="913" r="6"/>
    <circle cx="655" cy="913" r="6"/><circle cx="672" cy="913" r="6"/>
  </g>
  <g fill="#fff">
    <path d="M306 910 l-3 3 l3 3z"/><path d="M321 910 l3 3 l-3 3z"/>
    <path d="M656 910 l-3 3 l3 3z"/><path d="M671 910 l3 3 l-3 3z"/>
  </g>

  <circle cx="40" cy="956" r="18" fill="#2a2f36" stroke="#fff" stroke-width="2" role="img" aria-label="Author portrait"/>
  <circle cx="40" cy="1022" r="18" fill="#2a2f36" stroke="#fff" stroke-width="2" role="img" aria-label="Author portrait"/>

  <g fill="none" stroke="#2a2a2a" stroke-width="2.5">
    <rect x="371" y="944" width="27" height="25" rx="2"/>
    <rect x="371" y="1007" width="27" height="25" rx="2"/>
  </g>
  <g fill="#2a2a2a">
    <rect x="371" y="944" width="27" height="6"/><rect x="371" y="1007" width="27" height="6"/>
    <rect x="376" y="954" width="4" height="4"/><rect x="383" y="954" width="4" height="4"/><rect x="390" y="954" width="4" height="4"/>
    <rect x="376" y="961" width="4" height="4"/><rect x="383" y="961" width="4" height="4"/><rect x="390" y="961" width="4" height="4"/>
    <rect x="376" y="1017" width="4" height="4"/><rect x="383" y="1017" width="4" height="4"/><rect x="390" y="1017" width="4" height="4"/>
    <rect x="376" y="1024" width="4" height="4"/><rect x="383" y="1024" width="4" height="4"/><rect x="390" y="1024" width="4" height="4"/>
  </g>
</svg>

<!-- header -->
<div class="abs top-rule"></div>
<div class="abs brand">
  <span class="brand-square"></span>
  <span class="brand-name">QuillHarbor</span>
</div>
<div class="abs phone">
  <svg width="22" height="22" viewBox="0 0 22 22"><circle cx="11" cy="11" r="10" fill="none" stroke="var(--gold)" stroke-width="1.5"/><path d="M8 6 l2 3 l-1.5 1.5 q1 2.5 3 3.5 l1.5-1.5 l3 2 l-1.5 2 q-5 0-8-7z" fill="var(--gold)"/></svg>
  <span>555-013-4782</span>
</div>
<nav class="abs nav">
  <span>INTEGRATED MARKETING</span><span>SERVICES</span><span>NEWS &amp; EVENTS</span><span>RIDECIRCLE™</span><span>BLOG</span><span>CONTACT US</span>
</nav>

<!-- hero -->
<div class="abs hero-line">We Have A Passion For What We Do. Let Us<br>Do What We Do Best ...<span class="accent">Quill <b>HARBOR.</b></span></div>
<div class="abs btn" style="left:178px;top:195px"><span class="tip"><svg width="8" height="6"><path d="M0 3h6M4 1l2 2-2 2" stroke="#fff" fill="none"/></svg></span><span class="label">Find Out More</span></div>

<!-- services -->
<div class="abs svc-label" style="left:270px;top:280px">Social Media Marketing</div>
<div class="abs svc-label" style="left:49px;top:369px">OutBound Marketing</div>
<div class="abs svc-label" style="left:492px;top:369px">Mobile Marketing</div>
<div class="abs svc-label" style="left:270px;top:457px">InBound Marketing</div>
<div class="abs section-title" style="left:250px;top:409px">Our Services</div>

<!-- welcome -->
<section class="abs welcome">
  <h2>Welcome To QuillHarbor</h2>
  <p>Lorem ipsum dolor sit amet, consectetuer adipiscing elit, sed diam nonummy nibh euismod tincidunt ut laoreet dolore magna aliquam erat volutpat. Ut wisi enim ad minim veniam, quis nostrud exerci tation ullamcorper suscipit lobortis nisl ut aliquip ex ea commodo consequat. Duis autem vel eum iriure dolor in hendrerit in vulputate velit esse molestie consequat, vel illum dolore eu feugiat nulla facilisis at vero eros et accumsan et iusto odio dignissim qui blandit praesent luptatum zzril delenit augue duis dolore te feugait.</p>
</section>
<div class="abs btn" style="left:20px;top:745px"><span class="tip"><svg width="8" height="6"><path d="M0 3h6M4 1l2 2-2 2" stroke="#fff" fill="none"/></svg></span><span class="label">Read More</span></div>

<!-- quick contact -->
<section class="abs contact">
  <h3>Quick Contact Us</h3>
  <div class="rule"></div>
  <div class="field" style="top:46px;height:20px">Name</div>
  <div class="field" style="top:73px;height:20px">Email</div>
  <div class="field" style="top:99px;height:61px">Message</div>
  <div class="send">Send</div>
</section>

<!-- latest blog post -->
<div class="abs col-title" style="left:20px;top:902px">Latest Blog Post</div>
<div class="abs post-date" style="left:74px;top:936px">09/12/2014</div>
<div class="abs post-text" style="left:74px;top:949px">Lorem ipsum dolor sit amet, cctetuer adipiscingin elit, sed diam nummy nibh eui smod tinciduntiot vulputate</div>
<div class="abs divider" style="left:20px;top:990px;width:308px"></div>
<div class="abs post-date" style="left:74px;top:1003px">07/12/2014</div>
<div class="abs post-text" style="left:74px;top:1016px">Lorem ipsum dolor sit amet, cctetuer adipiscingin elit, sed diam nummy nibh eui smod tinciduntiot vulputate</div>

<!-- news & events -->
<div class="abs col-title" style="left:369px;top:902px">News &amp; Events</div>
<div class="abs event-title" style="left:417px;top:936px">Lorem ipsum dolor sit amet</div>
<div class="abs post-text" style="left:417px;top:953px">Lorem ipsum dolor sit amet, cctetuer adipiscingin elit, sed diam nummy nibh eui smod tinciduntiot vulputate</div>
<div class="abs divider" style="left:369px;top:990px;width:310px"></div>
<div class="abs event-title" style="left:417px;top:999px">Lorem ipsum dolor sit amet</div>
<div class="abs post-text" style="left:417px;top:1016px">Lorem ipsum dolor sit amet, cctetuer adipiscingin elit, sed diam nummy nibh eui smod tinciduntiot vulputate</div>

<!-- footer -->
<nav class="abs foot-nav">
  <span>Home</span><span>•</span><span>Services</span><span>•</span><span>News &amp; Events</span><span>•</span><span>Integratied Marketing</span><span>•</span><span>RideCircle</span><span>•</span><span>Blog</span><span>•</span><span>Contact Us</span>
</nav>
<div class="abs foot-social">
  <svg width="10" height="10"><circle cx="5" cy="5" r="4" fill="#fff"/></svg>
  <svg width="14" height="14"><line x1="0" y1="14" x2="14" y2="0" stroke="#6c8ea0"/></svg>
  <svg width="10" height="10"><circle cx="5" cy="5" r="4" fill="#fff"/></svg>
  <svg width="14" height="14"><line x1="0" y1="14" x2="14" y2="0" stroke="#6c8ea0"/></svg>
  <svg width="10" height="10"><circle cx="5" cy="5" r="4" fill="#fff"/></svg>
  <svg width="14" height="14"><line x1="0" y1="14" x2="14" y2="0" stroke="#6c8ea0"/></svg>
  <span>Share +</span>
</div>
<div class="abs foot-brand">
  <span class="brand-square"></span>
  <span class="brand-name">QuillHarbor</span>
</div>
<div class="abs foot-rule"></div>
<div class="abs copyright">© 2014 Quillharbor.com. All Rights Reserved &nbsp;|&nbsp; Terms and conditions &nbsp;|&nbsp; Privacy Policy</div>

</body>
</html>
```